WP website design Pine Harbor (Contest)

We need a wordpress design that will incorporate a professional color scheme with company logo in a clean layout. The design needs to consider that this will be developed on a responsive theme. Colors are blue and green of the logo and and an accent color (perhaps very light brown/tan). Client wants a 'modern' look.

Industry/Entity Type

It Company

Font styles to use
Serif
Sans Serif

Colors

Designer to choose colors to be used in the design.

Requirements
Must have
• Navigation: 1) Home; 2) Upcoming Auctions; 3) Past Auctions; 4) About Us; 5) Services; 6) Sellers; 7) Buyers; 8) Contact Us

Site will have slideshow - image is attached. Colors will be those in the logo, blue and green with maybe an accent color. A site the client mentions liking is trevalleauctions.com for the use of color and layout.

Widgets: 1) Featured Properties; 2) Call to action for Sellers 3) Testimonials blog/widget
Nice to have
• use of dropdown menus

```html
<!DOCTYPE html>
<html lang="en">
<head>
<meta charset="utf-8">
<title>Pine Harbor Auction &amp; Real Estate</title>
<link href="https://fonts.googleapis.com/css2?family=Arimo:ital,wght@0,400;0,700;1,400&family=Roboto+Condensed:wght@700&family=Roboto:wght@400;500;700&family=Michroma&display=swap" rel="stylesheet">
<style>
:root{
  --blue:#0b3a80;
  --blue-line:#2a62b0;
  --green:#077148;
  --green-text:#0f6b3f;
  --navy-text:#1d3575;
  --panel:#eeeeee;
  --panel-border:#dddddd;
  --dark:#232323;
  --white:#ffffff;
  --ink:#222222;
  --muted:#777777;
}
*{margin:0;padding:0;box-sizing:border-box}
html,body{width:877px;height:1200px;overflow:hidden;background:var(--white)}
body{position:relative;font-family:Arimo,Arial,sans-serif;color:var(--ink)}
.abs{position:absolute}

/* header */
.brand{left:76px;top:12px;display:flex;align-items:center;gap:8px}
.brand-dot{width:30px;height:30px;border-radius:50%;background:var(--blue)}
.brand-name{font-family:"Roboto Condensed",sans-serif;font-weight:700;font-size:20px;line-height:21px;color:var(--blue)}
.brand-sub{left:240px;top:20px;font-family:"Roboto Condensed",sans-serif;font-weight:700;font-size:19px;line-height:21px;color:var(--green-text);text-align:center}
.contact-phone{left:666px;top:33px;font-family:Roboto,sans-serif;font-weight:500;font-size:17px;color:var(--blue);display:flex;align-items:center;gap:6px}
.contact-mail{left:666px;top:59px;font-size:11px;color:var(--blue);display:flex;align-items:center;gap:6px}

/* nav */
.nav{left:0;top:97px;width:877px;height:26px;background:var(--blue);border-bottom:2px solid var(--blue-line)}
.nav ul{list-style:none;display:flex;position:absolute;left:73px;top:0;height:24px}
.nav li{font-family:Arimo,sans-serif;font-size:11.5px;color:#dfe8f5;line-height:24px;padding:0 10px;margin-right:23px;position:relative}
.nav li.active{background:var(--green);color:var(--white)}
.nav li.active::after{content:"";position:absolute;left:50%;bottom:0;margin-left:-4px;border:4px solid transparent;border-bottom-color:var(--white)}

/* hero */
.hero{left:0;top:123px;width:877px;height:479px;background:var(--green)}
.hero-media{left:72px;top:20px;width:735px;height:294px;border:3px solid var(--white);background:linear-gradient(180deg,#6f9a4c 0%,#a56f55 45%,#8b4a3a 70%,#4f7a34 100%)}
.hero-title{left:0;top:341px;width:877px;text-align:center;font-family:Roboto,sans-serif;font-weight:700;font-size:24px;color:var(--white);letter-spacing:.6px}
.hero-text{left:95px;top:387px;width:690px;text-align:center;font-size:9.6px;line-height:17.6px;color:var(--white)}

/* dividers */
.rule-h{left:77px;top:653px;width:723px;border-top:1px dotted #bbb}
.rule-v{left:565px;top:655px;height:453px;border-left:1px dotted #bbb}

/* featured */
.featured{left:72px;width:476px;height:174px;background:var(--panel);border:1px solid #e2e2e2}
.featured h2{position:absolute;left:12px;top:10px;font-family:Roboto,sans-serif;font-weight:500;font-size:15.5px;letter-spacing:1.2px;color:var(--navy-text)}
.featured h3{position:absolute;left:12px;top:43px;font-family:Michroma,sans-serif;font-weight:400;font-size:8.4px;letter-spacing:.4px;color:var(--ink)}
.thumb{position:absolute;left:13px;top:65px;width:123px;height:76px;border:3px solid var(--white);background:linear-gradient(180deg,#8fb3d6 0%,#b39a7a 55%,#5f8a3e 100%)}
.info{position:absolute;left:141px;top:68px;width:320px;font-size:8.6px;line-height:14.5px}
.info .kind{font-family:Roboto,sans-serif;font-size:9.6px;color:var(--green-text);letter-spacing:.3px;line-height:15px}
.info b{font-weight:700}
.info .desc{margin-top:3px;line-height:13px}
.btns{position:absolute;left:307px;top:141px;display:flex;gap:5px}
.btn{height:21px;border-radius:5px;color:var(--white);font-size:9px;display:flex;align-items:center;gap:5px;padding:0 8px;box-shadow:0 1px 2px rgba(0,0,0,.3)}
.btn-details{background:var(--blue);font-weight:700}
.btn-gallery{background:#222;font-family:Roboto,sans-serif;letter-spacing:.5px}

/* sidebar */
.widget{left:586px;width:213px;background:var(--panel);border:2px solid var(--panel-border)}
.widget-head{color:var(--white);font-family:Roboto,sans-serif;font-weight:700;font-size:13.5px;letter-spacing:.6px;padding:5px 14px}
.cta .widget-head{background:var(--blue);line-height:17px;height:40px}
.cta-link{position:absolute;left:14px;top:54px;font-family:Roboto,sans-serif;font-size:10.5px;letter-spacing:.6px;color:var(--green-text);text-decoration:underline}
.cta-media{position:absolute;left:11px;top:76px;width:186px;height:86px;border:3px solid var(--white);background:linear-gradient(180deg,#8fa3b3 0%,#8a6a5e 35%,#7a5a52 55%,#6d92b0 70%,#4e8a3a 85%,#3c7a2c 100%)}
.auction .widget-head{background:var(--green);height:33px;line-height:23px}
.auction{background:linear-gradient(180deg,#f4f4f4,#ecebea)}
.quote{position:absolute;left:18px;top:52px;width:182px;font-style:italic;font-size:8px;line-height:14.5px;color:#333}
.quote .mark{font-family:Georgia,serif;font-size:20px;color:#888;font-style:normal;line-height:0;vertical-align:-6px}
.author{position:absolute;right:62px;top:164px;font-style:italic;font-size:8.3px;color:#222;letter-spacing:-.2px}
.posted{position:absolute;right:62px;top:180px;font-style:italic;font-size:7.5px;color:var(--muted)}
.avatar{position:absolute;right:16px;top:150px;width:40px;height:35px;border:2px solid var(--white);background:linear-gradient(135deg,#d8a382,#6b8fb8)}

/* footer */
.footer{left:0;top:1108px;width:877px;height:92px;background:var(--dark)}
.footer-info{position:absolute;left:75px;top:17px;font-size:9.6px;line-height:16px;color:var(--white)}
.footer-info .copy{font-size:8.6px;margin-top:2px}
.footer-brand{position:absolute;left:620px;top:22px;display:flex;gap:18px;align-items:center}
.footer-brand .name{font-family:"Roboto Condensed",sans-serif;font-weight:700;font-size:15px;line-height:15px;color:#cfcfcf;text-align:center}
</style>
</head>
<body>

<header>
  <div class="abs brand">
    <span class="brand-dot"></span>
    <span class="brand-name">Summit Field<br>Real Estate</span>
  </div>
  <div class="abs brand-sub">Pine Harbor<br>Auction &amp;<br>Real Estate</div>
  <div class="abs contact-phone">
    <svg width="14" height="12" viewBox="0 0 14 12"><path d="M1 4c0-2 3-3 6-3s6 1 6 3v1h-3V4H4v1H1z" fill="#222"/><rect x="3" y="6" width="8" height="5" rx="1" fill="#222"/></svg>
    (850) 555-0142
  </div>
  <div class="abs contact-mail">
    <svg width="18" height="11" viewBox="0 0 18 11"><rect width="18" height="11" fill="#222"/><path d="M0 0l9 6 9-6" stroke="#fff" fill="none"/></svg>
    office@summitfieldpine.com
  </div>
</header>

<nav class="abs nav">
  <ul>
    <li class="active">Home</li>
    <li>Upcoming Auctions</li>
    <li>Past Auctions</li>
    <li>About Us</li>
    <li>Services</li>
    <li>Sellers</li>
    <li>Buyers</li>
    <li>Contact Us</li>
  </ul>
</nav>

<section class="abs hero">
  <div class="abs hero-media" role="img" aria-label="Slideshow photo of a red brick two-storey house with landscaped garden"></div>
  <h1 class="abs hero-title">Welcome to SF Pine Harbor Auction</h1>
  <p class="abs hero-text">simply dummy text of the printing and typesetting industry. Lorem Ipsum has been the industry's standard dummy text ever since the 1500s, when an unknown printer took a galley of type and scrambled it to make a type specimen book. It has survived not only five centuries, but also the leap into electronic typesetting, remaining essentially unchanged. It was popularised in the 1960s with the release of Lexton sheets containing Lorem Ipsum passages, and more recently with desktop publishing software like Quire Pagesetter including versions of Lorem Ipsum.</p>
</section>

<div class="abs rule-h"></div>
<div class="abs rule-v"></div>

<main>
  <article class="abs featured" style="top:672px">
    <h2>FEATURED PROPERTIES</h2>
    <h3>SHOP EQUIPMENT/TOOLS * PORK PROCESSING ITEMS</h3>
    <div class="thumb" role="img" aria-label="Photo of a large family home for auction"></div>
    <div class="info">
      <div class="kind">LIVE ON-SITE AUCTION</div>
      <div><b>Begins:</b>&nbsp; Saturday, March 16, 2013 at 10:00 AM EDT</div>
      <div><b>Location:</b>&nbsp; 2316 Larkin Road Fairdale, KY 40118</div>
      <div class="desc">Keiyo BS3F High Lift, 600 Series Harlan tractor w/Brisco Loader, Dune buggy, 1207 KR Cutditioner: SHOP.</div>
    </div>
    <div class="btns">
      <span class="btn btn-details"><svg width="13" height="9" viewBox="0 0 13 9"><rect width="5" height="9" rx="1" fill="#fff"/><rect x="7" y="0" width="6" height="1.6" fill="#fff"/><rect x="7" y="3.7" width="6" height="1.6" fill="#fff"/><rect x="7" y="7.4" width="6" height="1.6" fill="#fff"/></svg>Details</span>
      <span class="btn btn-gallery"><svg width="13" height="11" viewBox="0 0 13 11"><rect x="1" y="2" width="11" height="8" rx="1" fill="none" stroke="#fff"/><circle cx="6.5" cy="6" r="2" fill="#fff"/></svg>GALLERY</span>
    </div>
  </article>

  <article class="abs featured" style="top:882px">
    <h2>FEATURED PROPERTIES</h2>
    <h3>SHOP EQUIPMENT/TOOLS * PORK PROCESSING ITEMS</h3>
    <div class="thumb" role="img" aria-label="Photo of a large family home for auction"></div>
    <div class="info">
      <div class="kind">LIVE ON-SITE AUCTION</div>
      <div><b>Begins:</b>&nbsp; Saturday, March 16, 2013 at 10:00 AM EDT</div>
      <div><b>Location:</b>&nbsp; 2316 Larkin Road Fairdale, KY 40118</div>
      <div class="desc">Keiyo BS3F High Lift, 600 Series Harlan tractor w/Brisco Loader, Dune buggy, 1207 KR Cutditioner: SHOP.</div>
    </div>
    <div class="btns">
      <span class="btn btn-details"><svg width="13" height="9" viewBox="0 0 13 9"><rect width="5" height="9" rx="1" fill="#fff"/><rect x="7" y="0" width="6" height="1.6" fill="#fff"/><rect x="7" y="3.7" width="6" height="1.6" fill="#fff"/><rect x="7" y="7.4" width="6" height="1.6" fill="#fff"/></svg>Details</span>
      <span class="btn btn-gallery"><svg width="13" height="11" viewBox="0 0 13 11"><rect x="1" y="2" width="11" height="8" rx="1" fill="none" stroke="#fff"/><circle cx="6.5" cy="6" r="2" fill="#fff"/></svg>GALLERY</span>
    </div>
  </article>
</main>

<aside>
  <div class="abs widget cta" style="top:669px;height:184px">
    <div class="widget-head">CALL TO ACTION FOR SELLERS</div>
    <div class="cta-link">TRACTOR * HI LIFT * MACHINERY</div>
    <div class="cta-media" role="img" aria-label="Photo of farmland with a pond and green field"></div>
  </div>

  <div class="abs widget auction" style="top:877px;height:204px">
    <div class="widget-head">FEATURED AUCTION</div>
    <p class="quote"><span class="mark">&ldquo;</span> Ipsum is simply dummy text of the printing and typesetting industry. Lorem Ipsum has been the industry's standard dummy text ever since the 1500s, when an unknown printer took a galley of type and scrambled it to make a type ... <span class="mark">&rdquo;</span></p>
    <div class="author">By Dale Herrin</div>
    <div class="posted">Posted on Nov25, 2012</div>
    <div class="avatar" role="img" aria-label="Portrait photo of the testimonial author"></div>
  </div>
</aside>

<footer class="abs footer">
  <div class="footer-info">
    Halvorsen Real Estate &amp; Auction Inc.<br>
    4810 Cedar Mill Rd., Riverton KY 40219<br>
    team@halvorsenauc.com &nbsp; Phone: (502) 555 0187
    <div class="copy">Copyright (c) Summit Field Real Estate Pine Harbor , Inc. 2014. All Right Reserved</div>
  </div>
  <div class="footer-brand">
    <span class="name">Summit Field<br>Real Estate</span>
    <span class="name">Pine Harbor<br>Auction &amp;<br>Real Estate</span>
  </div>
</footer>

</body>
</html>
```